Velmar Ops Business Cards

We need to design some upbeat business cards. We are an Industrial Rope Access Company/Height Safety Company that specialize in Rope Access, Confined Space, Anchor Points, Safety Systems, PPE Inspecions and Rigging.
Company name is Velmar Ops Ltd
Card is for Gareth Lomas the Company Director
His mobile number is 027 418 9072 and email is gareth@velmarops.co.nz. Website address is www.velmarops.co.nz.
We will post some pictures below to ensure you get a good idea of what we do.

```html
<!DOCTYPE html>
<html lang="en">
<head>
<meta charset="utf-8">
<title>Velmar Ops Business Cards</title>
<link href="https://fonts.googleapis.com/css2?family=Lato:wght@400;700;900&display=swap" rel="stylesheet">
<style>
  :root {
    --backdrop: #46445f;
    --card-dark: #070707;
    --card-light: #ffffff;
    --ink-dark: #1b1b1b;
    --ink-name: #454545;
    --ink-muted: #5a5a5a;
    --rule: #3a3a3a;
    --on-dark: #ffffff;
  }
  * { box-sizing: border-box; margin: 0; padding: 0; }
  html, body {
    width: 1200px;
    height: 1000px;
    overflow: hidden;
  }
  body {
    position: relative;
    background: var(--backdrop);
    font-family: "Lato", Arial, sans-serif;
  }
  .card {
    position: absolute;
    width: 672px;
    height: 382px;
    border-radius: 32px;
  }
  .card--front {
    left: 263px;
    top: 85px;
    background: var(--card-dark);
  }
  .card--back {
    left: 262px;
    top: 528px;
    background: var(--card-light);
  }
  .brand-name {
    position: absolute;
    font-weight: 900;
    white-space: nowrap;
    letter-spacing: 0.5px;
  }
  .card--front .brand-name {
    left: 0;
    right: 0;
    top: 158px;
    text-align: center;
    font-size: 58px;
    line-height: 1;
    color: var(--on-dark);
  }
  .card--back .brand-name {
    right: 46px;
    top: 46px;
    font-size: 42px;
    line-height: 1;
    color: var(--ink-dark);
  }
  .holder-name {
    position: absolute;
    left: 36px;
    top: 124px;
    font-size: 34px;
    font-weight: 400;
    color: var(--ink-name);
    line-height: 1;
  }
  .holder-role {
    position: absolute;
    left: 41px;
    top: 172px;
    font-size: 19px;
    color: var(--ink-muted);
    line-height: 1;
    white-space: nowrap;
  }
  .role-rule {
    position: absolute;
    left: 288px;
    top: 187px;
    width: 343px;
    height: 2px;
    background: var(--rule);
  }
  .contact-list {
    position: absolute;
    left: 36px;
    top: 262px;
    list-style: none;
  }
  .contact-item {
    display: flex;
    align-items: center;
    height: 36px;
    font-size: 22px;
    color: var(--ink-name);
  }
  .contact-icon {
    width: 18px;
    height: 18px;
    margin-right: 16px;
    fill: var(--ink-name);
    flex: none;
  }
  .website {
    position: absolute;
    right: 43px;
    top: 323px;
    font-size: 19px;
    color: var(--ink-muted);
    line-height: 1;
  }
</style>
</head>
<body>
  <section class="card card--front" aria-label="Card front">
    <div class="brand-name">Velmar Ops</div>
  </section>

  <section class="card card--back" aria-label="Card back">
    <div class="brand-name">Velmar Ops</div>
    <h1 class="holder-name">Gareth Lomas</h1>
    <p class="holder-role">Director -&nbsp; Velmar Ops Ltd</p>
    <div class="role-rule"></div>
    <ul class="contact-list">
      <li class="contact-item">
        <svg class="contact-icon" viewBox="0 0 24 24" aria-hidden="true">
          <path d="M6.6 10.8a15.2 15.2 0 0 0 6.6 6.6l2.2-2.2c.3-.3.7-.4 1-.2 1.1.4 2.3.6 3.6.6.6 0 1 .4 1 1V20c0 .6-.4 1-1 1C10.6 21 3 13.4 3 4c0-.6.4-1 1-1h3.5c.6 0 1 .4 1 1 0 1.3.2 2.5.6 3.6.1.3 0 .7-.2 1z"/>
        </svg>
        027 418 9072
      </li>
      <li class="contact-item">
        <svg class="contact-icon" viewBox="0 0 24 24" aria-hidden="true">
          <path d="M2 6h20v12H2z M2 6l10 7 10-7" fill="none" stroke="currentColor"/>
          <path d="M2 6.5h20v11.5H2z"/>
          <path d="M2.5 6.5l9.5 6.5 9.5-6.5" fill="none" stroke="#ffffff" stroke-width="1.6"/>
        </svg>
        gareth@velmarops.co.nz
      </li>
    </ul>
    <p class="website">www.velmarops.co.nz</p>
  </section>
</body>
</html>
```